Powerpoint template for Tovra - Helping people when they need it the most

Our most urgent need is a powerpoint template with logo, but over time we will also need web design, business card design etc.

We are Tovra Solutions AS, a company delivering innovative services for people when they need it the most.

Our first service, EaseBox (EaseBox by Tovra Solutions), will help people get through all the paperwork and obstacles they meet when they become seriously ill or loose someone close to them. This could typically be automation and digital handling of social security forms, insurance and banking etc.This will free up time for people to focus on recovery or spend time with family.

Our core values are: "Passionate", "Caring" and "Make a difference".
Our vision is (in Norwegian): «EaseBox hjelper deg når du trenger det som mest” which means "EaseBox is there for you when you need it the most".

We need a simple and pure design that:
- Signals to end-users that we are there to help them.
- Signals to investors that Tovra is an innovative company with services based on the latest technology.

The design should include an appropriate logo.
We would like a warm color to be used (we have been using red until now).

Check out our website for more background information: www.tovra-example.no

See also the attached homemade powerpoint presentation that we need to turn into a spectacular pitch! Please do NOT keep much from the original slides.

Target Market(s)

Keep in mind that we are a Scandinavian company.
We want a simple, warm/caring and innovative design that also conveys our tech side.

Industry/Entity Type

Business

Requirements
Must have
• Pictures (of people) - This is all about people
• For our investor pitch we will eventually need slides regarding
• - The problem
• - Our insight / domain knowledge
• - Product/Solution/How it works
• - Vision
• - Market/ Market size / Market potential
• - Business Model
• - Competition / Competetive advantages
• - Plan / Milestones / Timeline
• - The team
• - Strength & weaknesses (including network)
• - Investors / Partners
• - Value proposition
• - Elevator pitch
• - Why Invest (What's in it for the investor)
• - Concerns & Responses
• - Tovra in numbers
• - Financials
• - Q& A
• The slides should reflect that we see ourselves as a tech company (although a caring one) as machine learning, artificial intelligence and robotics.
• In the phase we are in right now we will be interviewing lots of potential users to understand the underlying needs. It would be good to have some pictures to illustrate the interview and user testing situations.
• These are just tips for you to understand what we are occupied with. Please feel free to use you're creativity!
Should not have
• Very bright and exotic colors. We are a Nordic/Scandinavian company

```html
<!DOCTYPE html>
<html lang="no">
<head>
<meta charset="utf-8">
<title>Tovra – pitch template slides</title>
<link rel="stylesheet" href="https://fonts.googleapis.com/css2?family=Open+Sans:wght@300;400;600;700&family=Arimo:wght@400;700&display=swap">
<style>
  :root {
    --navy: #13306b;
    --ink: #2b2b2b;
    --muted: #555a61;
    --red: #d2262b;
    --ice-1: #eef6fb;
    --ice-2: #bfe2ef;
    --ice-card: rgba(190, 228, 242, 0.55);
    --rust-1: #b4481c;
    --rust-2: #6f2a10;
    --photo-blue: #b7d3e4;
    --photo-dark: #3a3f48;
    --white: #ffffff;
  }
  * { margin: 0; padding: 0; box-sizing: border-box; }
  html, body { width: 1200px; height: 1200px; overflow: hidden; background: var(--white); }
  body { position: relative; font-family: "Open Sans", sans-serif; color: var(--ink); }

  .slide { position: absolute; overflow: hidden; background: var(--white); box-shadow: 0 12px 28px rgba(0,0,0,0.22); }

  .brand-name {
    position: absolute; height: 38px; display: flex; align-items: center; gap: 8px;
    font-family: "Open Sans", sans-serif; font-weight: 600; font-size: 20px; color: var(--navy);
  }
  .brand-name::before { content: ""; width: 10px; height: 10px; background: var(--red); }
  .brand-name.on-photo { color: var(--white); }

  /* Slide 1 – strengths & weaknesses */
  .slide-strengths { left: 0; top: 0; width: 691px; height: 390px; }
  .slide-strengths .brand-name { left: 20px; top: 19px; }
  .ice-backdrop { position: absolute; inset: 0; background: linear-gradient(180deg, var(--ice-1) 0%, #dcedf5 35%, var(--ice-2) 100%); }
  .slide-title { position: absolute; font-family: "Open Sans", sans-serif; font-weight: 300; color: var(--navy); }
  .slide-strengths .slide-title { left: 0; width: 672px; top: 44px; text-align: center; font-size: 30px; }
  .sw-card { position: absolute; top: 112px; width: 266px; height: 244px; border-radius: 34px; background: var(--ice-card); padding: 18px 10px 0 22px; overflow: hidden; }
  .sw-card.strong { left: 64px; }
  .sw-card.weak { left: 382px; }
  .sw-card h2 { font-family: "Arimo", sans-serif; font-weight: 400; font-size: 28px; color: var(--navy); }
  .sw-card .sign { position: absolute; right: 26px; top: 20px; color: var(--white); font-size: 20px; font-weight: 300; }
  .sw-card .rule { width: 38px; height: 2px; background: var(--muted); margin: 8px 0 12px; }
  .sw-card ul { list-style: none; font-family: "Arimo", sans-serif; font-size: 11.6px; line-height: 20.8px; color: #3f4650; }
  .sw-card li { position: relative; padding-left: 18px; white-space: nowrap; }
  .sw-card li::before { content: "•"; position: absolute; left: 0; font-size: 9px; }
  .sw-card li.cont::before { content: none; }

  /* Slide 2 – progress */
  .slide-progress { left: 509px; top: 228px; width: 691px; height: 388px; }
  .slide-progress .brand-name { left: 19px; top: 18px; }
  .slide-progress .slide-title { left: 117px; top: 30px; font-size: 29px; }
  .photo-column { position: absolute; left: 249px; top: 0; width: 212px; height: 100%; background: linear-gradient(180deg, var(--photo-blue) 0%, #dfe7ee 30%, var(--photo-dark) 60%, #8b6a55 85%, #1f2c48 100%); }
  .milestone { position: absolute; width: 160px; text-align: center; }
  .milestone svg { display: block; margin: 0 auto; }
  .milestone h3 { font-family: "Arimo", sans-serif; font-weight: 700; font-size: 9.5px; letter-spacing: 2px; color: var(--ink); margin-top: 6px; }
  .milestone p { font-family: "Arimo", sans-serif; font-size: 8.5px; line-height: 15.5px; color: var(--muted); margin-top: 5px; }
  .m1 { left: 80px; top: 104px; }
  .m2 { left: 459px; top: 114px; }
  .m3 { left: 80px; top: 240px; }
  .m4 { left: 459px; top: 240px; }
  .tagline { position: absolute; right: 11px; bottom: 8px; color: var(--red); font-size: 10.5px; }

  /* Slide 3 – team */
  .slide-team { left: 0; top: 521px; width: 691px; height: 389px; }
  .slide-team .brand-name { left: 20px; top: 18px; }
  .team-divider { position: absolute; left: 346px; top: 95px; width: 1px; height: 240px; background: #dddddd; }
  .member { position: absolute; top: 96px; width: 240px; text-align: center; }
  .member.one { left: 103px; }
  .member.two { left: 347px; }
  .portrait { width: 92px; height: 98px; margin: 0 auto; background: linear-gradient(160deg, #8c7a70, #3a3030); clip-path: polygon(25% 0, 75% 0, 100% 50%, 75% 100%, 25% 100%, 0 50%); }
  .member h3 { margin-top: 18px; font-family: "Arimo", sans-serif; font-weight: 700; font-size: 9.5px; letter-spacing: 2px; color: var(--ink); }
  .member .role { font-family: "Arimo", sans-serif; font-size: 8.5px; color: var(--muted); margin-top: 3px; }
  .member .accent { width: 26px; height: 2px; background: var(--red); margin: 12px auto 8px; }
  .member .bio { text-align: left; font-family: "Arimo", sans-serif; font-size: 5.8px; line-height: 11.6px; color: var(--muted); width: 224px; margin-left: 6px; }

  /* Slide 4 – thank you */
  .slide-thanks { left: 509px; top: 810px; width: 691px; height: 390px; }
  .slide-thanks .brand-name { left: 19px; top: 17px; }
  .warm-backdrop { position: absolute; inset: 0; background: radial-gradient(ellipse at 55% 70%, var(--rust-2) 0%, var(--rust-1) 55%, #c45c27 100%); }
  .thanks-frame { position: absolute; left: 286px; top: 276px; width: 119px; height: 23px; border: 1px solid var(--white); color: var(--white); font-size: 9px; letter-spacing: 4px; display: flex; align-items: center; justify-content: center; }
</style>
</head>
<body>

<section class="slide slide-strengths">
  <div class="ice-backdrop" role="img" aria-label="Pale blue photograph of glacier ice"></div>
  <div class="brand-name">Tovra</div>
  <h1 class="slide-title">Strengths and weaknesses</h1>
  <div class="sw-card strong">
    <h2>Fortrinn</h2><span class="sign">+</span>
    <div class="rule"></div>
    <ul>
      <li>Inngående kjennskap til bransjen – bank</li>
      <li class="cont">og livslivselskap.</li>
      <li>Nettverk i bransjen – bank, livselskap og</li>
      <li class="cont">forsikring.</li>
      <li>Brukerinnsikt – problemet.</li>
      <li>Personlig historie – alvorlig syk datter.</li>
    </ul>
  </div>
  <div class="sw-card weak">
    <h2>Utfordringer</h2><span class="sign">–</span>
    <div class="rule"></div>
    <ul>
      <li>Behov for starthjelp til å pitche.</li>
      <li>Muligheten til å delta i nettverk, sparre,</li>
      <li class="cont">bli utfordret, mm.</li>
      <li>Støtte i utvikling av</li>
      <li class="cont">forretningsmodell.</li>
      <li>Hjelp til å rekruttere</li>
      <li>Behov for funding</li>
    </ul>
  </div>
</section>

<section class="slide slide-progress">
  <div class="brand-name">Tovra</div>
  <h1 class="slide-title">Progress</h1>
  <div class="milestone m1">
    <svg width="52" height="52" viewBox="0 0 52 52" fill="none" stroke="#222" stroke-width="1.5">
      <circle cx="15" cy="7" r="5"/><circle cx="37" cy="7" r="5"/>
      <path d="M9 48V24q0-8 6-8t6 8l5 6 5-6q0-8 6-8t6 8v24M15 48V34M37 48V34"/>
    </svg>
    <h3>MILEPÆL 1</h3>
    <p>Etablere team og resursser.<br>Innhente brukerinnsikt.</p>
  </div>
  <div class="milestone m2">
    <svg width="40" height="40" viewBox="0 0 40 40" fill="none" stroke="#222" stroke-width="1.5">
      <path d="M4 4l26 26M30 30l6 6-3 3-6-6zM4 4l5 1 1 5"/>
      <path d="M36 4l-22 22M14 26l-6 2-4 6 2 2 6-4 2-6M30 4a5 5 0 0 0 6 6"/>
    </svg>
    <h3>MILEPÆL 2</h3>
    <p>Utvikle og teste prototype av<br>EaseBox. Skaffe<br>samarbeidspartnere.</p>
  </div>
  <div class="milestone m3">
    <svg width="48" height="42" viewBox="0 0 48 42" fill="none" stroke="#222" stroke-width="1.5">
      <path d="M4 34a20 20 0 1 1 40 0"/><path d="M24 26l8-7"/><circle cx="24" cy="27" r="3"/>
      <rect x="16" y="34" width="16" height="5"/><path d="M9 19l3 2M24 10v4M39 19l-3 2"/>
    </svg>
    <h3>MILEPÆL 3</h3>
    <p>Rekruttere pilotpartnere.<br>Soft launch</p>
  </div>
  <div class="photo-column" role="img" aria-label="Photograph of a hand typing on a laptop with a chart on screen"></div>
  <div class="milestone m4">
    <svg width="40" height="42" viewBox="0 0 40 42" fill="none" stroke="#222" stroke-width="1.5">
      <path d="M32 4q-14 2-20 20l6 6q18-6 20-20zM12 24l-6 2 4-8 6-1M18 30l-2 6 8-4 1-6M12 30l-6 8"/>
    </svg>
    <h3>MILEPÆL 4</h3>
    <p>Tilby EaseBox på markedet</p>
  </div>
  <div class="tagline">EaseBox by Tovra</div>
</section>

<section class="slide slide-team">
  <div class="brand-name">Tovra</div>
  <div class="team-divider"></div>
  <div class="member one">
    <div class="portrait" role="img" aria-label="Portrait photo of team member Ingrid Holmvik Aas"></div>
    <h3>INGRID HOLMVIK AAS</h3>
    <p class="role">Master in Marketing Management</p>
    <div class="accent"></div>
    <p class="bio">Forretningsutvikler med sterk interesse for teknologi som skaper gode brukeropplevelser. Lang prosjekterfaring fra tverrfaglige team og smidig arbeid. Bygger relasjoner og nettverk på tvers av fagområder og nivåer. Bred erfaring med presentasjoner og innsikt for beslutningstakere. Kreativ, visuell og modig i ukjent terreng.</p>
  </div>
  <div class="member two">
    <div class="portrait" role="img" aria-label="Portrait photo of team member Siri Tveitane"></div>
    <h3>SIRI TVEITANE</h3>
    <p class="role">Datateknikk og teknisk kybernetikk</p>
    <div class="accent"></div>
    <p class="bio">Prosjektleder med IT-bakgrunn som liker å drive nye initiativ. Mange års erfaring med ledelse av team og prosjektgrupper med gode resultater. Opptatt av hvordan teknologi kan gjøre hverdagen enklere. Liker struktur i kaos, målrettet og utholdende.</p>
  </div>
</section>

<section class="slide slide-thanks">
  <div class="warm-backdrop" role="img" aria-label="Warm rust-toned photograph of a couple embracing in a field, seen from behind"></div>
  <div class="brand-name on-photo">Tovra</div>
  <div class="thanks-frame">THANK YOU</div>
</section>

</body>
</html>
```